Torvel, Inc. new buisness cards - brand guide included

We need new business cards. SLEAK SIMPLE FINANCE. They must include a place for NAME, TITLE, CELL, OFFICE PHONE, EMAIL. they also must include our services across the bottom. AIR, OCEAN, FTL, LTL, EXPRESS. for reference this will be being handed to some of the most prestigious shipping companies in a america.

Target Market(s)

Finance and corporate

Contact Information for Business Card

We need new business cards. SLEAK SIMPLE FINANCE. They must include a place for NAME, TITLE, CELL, OFFICE PHONE, EMAIL. they also must include our services across the bottom. AIR, OCEAN, FTL, LTL, EXPRESS.

Requirements
Must have
• We need new business cards. SLEAK SIMPLE FINANCE. They must include a place for NAME, TITLE, CELL, OFFICE PHONE, EMAIL. they also must include our services across the bottom. AIR, OCEAN, FTL, LTL, EXPRESS.
Nice to have
• USE THE COLORS AND LOGO IN THE BRAND GUIDE :)

```html
<!DOCTYPE html>
<html lang="en">
<head>
<meta charset="utf-8">
<title>Torvel, Inc. — Business Card</title>
<link rel="stylesheet" href="https://fonts.googleapis.com/css2?family=Libre+Baskerville:wght@400;700&display=swap">
<style>
  :root {
    --backdrop: #e8ecec;
    --tan: #c1b292;
    --paper: #ffffff;
    --ink: #2a2a2a;
    --ink-soft: #444444;
    --white: #ffffff;
  }
  * { margin: 0; padding: 0; box-sizing: border-box; }
  html, body {
    width: 1200px; height: 900px; overflow: hidden;
    background: var(--backdrop);
    font-family: "Libre Baskerville", Georgia, serif;
  }
  .stage {
    position: relative; width: 1200px; height: 900px;
    display: flex; align-items: center; justify-content: center; gap: 60px;
  }
  .card {
    position: relative; width: 520px; height: 297px;
    box-shadow: 0 2px 6px rgba(0,0,0,0.12);
  }
  .card--front { background: var(--tan); display: flex; align-items: center; justify-content: center; }
  .card--back { background: var(--paper); color: var(--ink); }

  .wordmark {
    font-weight: 400; letter-spacing: 0.14em; line-height: 1;
  }
  .card--front .wordmark { color: var(--white); font-size: 46px; }
  .card--back .wordmark {
    position: absolute; top: 40px; right: 40px;
    color: var(--ink); font-size: 30px;
  }

  .identity {
    position: absolute; left: 0; top: 166px;
    display: flex; align-items: flex-start;
  }
  .identity__bar { width: 22px; height: 40px; background: var(--ink); margin-right: 14px; margin-top: 2px; }
  .identity__name { font-weight: 700; font-size: 15px; letter-spacing: 0.03em; text-transform: uppercase; }
  .identity__title { font-size: 11.5px; color: var(--ink-soft); margin-top: 3px; }

  .contact {
    position: absolute; left: 36px; top: 222px;
    list-style: none; font-size: 11.5px; color: var(--ink-soft);
  }
  .contact li { display: flex; align-items: center; gap: 8px; height: 17px; }
  .contact svg { width: 10px; height: 10px; flex: none; }

  .services {
    position: absolute; right: 40px; bottom: 46px;
    border-top: 1.5px solid var(--ink);
    padding-top: 6px; padding-left: 12px;
    font-weight: 700; font-size: 11px; letter-spacing: 0.04em; white-space: nowrap;
  }
  .services span { margin: 0 4px; font-weight: 400; }
</style>
</head>
<body>
<main class="stage">
  <section class="card card--front" aria-label="Card front">
    <div class="wordmark">TORVEL</div>
  </section>

  <section class="card card--back" aria-label="Card back">
    <div class="wordmark">TORVEL</div>

    <div class="identity">
      <div class="identity__bar"></div>
      <div>
        <div class="identity__name">Daniel R. Hale</div>
        <div class="identity__title">Founder &amp; Director</div>
      </div>
    </div>

    <ul class="contact">
      <li>
        <svg viewBox="0 0 10 10" aria-hidden="true"><rect x="1.5" y="1.5" width="7" height="7" fill="none" stroke="#333" stroke-width="1.2"/></svg>
        +1 55-610-2870
      </li>
      <li>
        <svg viewBox="0 0 10 10" aria-hidden="true"><path d="M1 4 Q5 0 9 4 L8 5 L6.5 4 L6.5 3.2 Q5 2.6 3.5 3.2 L3.5 4 L2 5 Z M2.5 5.5 H7.5 V9 H2.5 Z" fill="#333"/></svg>
        +1 55-610-2870
      </li>
      <li>
        <svg viewBox="0 0 10 10" aria-hidden="true"><rect x="0.5" y="2" width="9" height="6.5" fill="#333"/><path d="M0.8 2.3 L5 5.6 L9.2 2.3" fill="none" stroke="#fff" stroke-width="0.9"/></svg>
        info@torvelfreight.com
      </li>
    </ul>

    <div class="services">AIR<span>|</span>OCEAN<span>|</span>FTL<span>|</span>LTL<span>|</span>EXPRESS</div>
  </section>
</main>
</body>
</html>
```